Natural cosmetics company is looking for a designer to produce the labels of the products and

Hello, Nus need a label and logo design for our brand RW ORGANIC. It is a brand specializing in the sale of 100% Natural cosmetic products on the internet. The first range is based on snail slime. I am looking for a clean design in green tones. The final design must be forwarded to the supplier for printing and shipping of the products. I realized a first idea for a logo, but I am interested in other ideas / suggestions. You have carte blanche :)
Here are the rules to follow for sending labels to the supplier:
• Sizes:
- Airless bottle: 10.3 x 5.5 cm
- Jar: 20x2.5cm
• Files must be in Corel Draw (. cdr) and / or vector PDF format
You must attach the file of the fonts used for the text in the label - We need this file as many fonts are difficult to find and we might need to move some text around for printing purposes
• The logo of your brand must be in a vector format along with all other components.
• Please do not add any borders or any cut marks to the design. We will do it on our end as we need to follow specific indications with our printing suppliers.
• All text and graphics must be at least 6mm from the edge
• The dimensions indicated by us must be respected in the overall size of the label
• The resolution to be used should be 300 cpi and in CMYK
• The text size should be readable and at least 4.5 points.

```html
<!DOCTYPE html>
<html lang="en">
<head>
<meta charset="utf-8">
<title>RW ORGANIC – Snail Slime Labels</title>
<link rel="stylesheet" href="https://fonts.googleapis.com/css2?family=Merriweather:wght@300;400&family=Caveat+Brush&family=Homemade+Apple&display=swap">
<style>
  :root {
    --paper: #ffffff;
    --ink: #2b2b2b;
    --ink-soft: #4a4a4a;
    --leaf: #1f9a3c;
    --leaf-deep: #3d6b52;
    --pattern-tint: #f7faec;
    --snail-main: #2e9e4a;
    --snail-light: #cfe9cf;
  }
  * { box-sizing: border-box; margin: 0; padding: 0; }
  html, body { width: 1200px; height: 486px; overflow: hidden; background: var(--paper); }
  .canvas { position: relative; width: 1200px; height: 486px; background: var(--paper); font-family: "Merriweather", Georgia, serif; color: var(--ink); }

  .label { position: absolute; background: var(--pattern-tint); }
  .label--wide { left: 50px; top: 53px; width: 792px; height: 99px; }
  .label--jar { left: 279px; top: 232px; width: 433px; height: 201px; }

  .copy { position: absolute; font-weight: 300; line-height: 1.06; color: var(--ink-soft); }
  .copy strong { font-weight: 400; color: var(--ink); display: block; }
  .copy--main { font-size: 8.4px; }
  .copy--fine { font-size: 6.6px; line-height: 1.12; }

  .snail-art {
    position: absolute;
    background: linear-gradient(120deg, var(--snail-main) 0%, var(--snail-light) 100%);
    border-radius: 50% 40% 30% 50% / 60% 60% 40% 40%;
  }

  .brand-mark { position: absolute; display: flex; align-items: center; justify-content: center; }
  .brand-mark__circle { position: absolute; border: 1.5px solid var(--ink); border-radius: 50%; background: var(--paper); }
  .brand-mark__name { position: relative; font-family: "Merriweather", Georgia, serif; font-weight: 400; color: var(--leaf-deep); white-space: nowrap; }

  .product-name { position: absolute; font-family: "Caveat Brush", cursive; color: var(--leaf); line-height: 1; white-space: nowrap; }
  .product-rule { position: absolute; height: 2px; background: var(--leaf); }
  .product-claim { position: absolute; font-family: "Homemade Apple", cursive; color: var(--ink); white-space: nowrap; line-height: 1; }
</style>
</head>
<body>
<main class="canvas">

  <!-- Bottle label (wide) -->
  <section class="label label--wide" role="img" aria-label="Faint pale green snail pattern background"></section>

  <p class="copy copy--main" style="left:79px; top:67px; width:190px;">
    <strong>Natural active ingredients in slime</strong>
    Pure snail slime contains active ingredients beneficial to the skin: allantoin, collagen, glycolic acid, elastin, vitamin A and vitamin C, natural antibiotic peptides. It is these components that improve skin texture, help heal skin lesions and restore radiance to the complexion.
  </p>

  <div class="snail-art" role="img" aria-label="Green snail illustration" style="left:314px; top:84px; width:100px; height:42px;"></div>
  <div class="brand-mark" style="left:350px; top:70px; width:54px; height:54px;">
    <span class="brand-mark__circle" style="inset:0;"></span>
    <span class="brand-mark__name" style="font-size:6.5px;">RW ORGANIC</span>
  </div>

  <h2 class="product-name" style="left:428px; top:68px; font-size:34px;">Snail Slime</h2>
  <span class="product-rule" style="left:433px; top:103px; width:127px;"></span>
  <p class="product-claim" style="left:421px; top:117px; font-size:9px;">100% Natural Cosmetic Product</p>

  <p class="copy copy--fine" style="left:642px; top:73px; width:178px;">
    Lorem Ipsum contains active ingredients Lorem Ipsum contains active ingredients Lorem Ipsum contains active ingredients Lorem Ipsum beneficial to the skin: allantoin, collagen, glycolic acid, elastin, vitamin A and natural antibiotic Lorem Ipsum contains active ingredients beneficial
  </p>

  <!-- Brand logo -->
  <div class="brand-mark" style="left:44px; top:214px; width:210px; height:210px;">
    <span class="brand-mark__circle" style="inset:0; border-width:4px;"></span>
    <span class="brand-mark__name" style="font-size:20px;">RW ORGANIC</span>
  </div>

  <!-- Jar label -->
  <section class="label label--jar" role="img" aria-label="Faint pale green snail pattern background"></section>

  <p class="copy copy--main" style="left:310px; top:250px; width:88px;">
    <strong>Natural active ingredients in slime</strong>
    Pure snail slime contains active ingredients beneficial to the skin: allantoin, collagen, glycolic acid, elastin, vitamin A and vitamin C, natural antibiotic peptides. It is these components that improve skin texture, help heal skin lesions and restore radiance to the complexion.
  </p>

  <div class="snail-art" role="img" aria-label="Green snail illustration" style="left:438px; top:278px; width:100px; height:34px;"></div>
  <div class="brand-mark" style="left:472px; top:258px; width:54px; height:54px;">
    <span class="brand-mark__circle" style="inset:0;"></span>
    <span class="brand-mark__name" style="font-size:6.5px;">RW ORGANIC</span>
  </div>

  <h2 class="product-name" style="left:419px; top:318px; font-size:40px;">Snail Slime</h2>
  <span class="product-rule" style="left:426px; top:358px; width:152px;"></span>
  <p class="product-claim" style="left:412px; top:393px; font-size:10.5px;">100% Natural Cosmetic Product</p>

  <p class="copy copy--fine" style="left:616px; top:254px; width:62px;">
    Lorem Ipsum Lorem Ipsum Lorem Ipsum Lorem Ipsum Lorem Ipsum Lorem Ipsum Lorem Ipsum Lorem Ipsum Lorem Ipsum contains active ingredients beneficial to the skin: allantoin, collagen, glycolic acid, elastin, vitamin A and natural antibiotic
  </p>

</main>
</body>
</html>
```